Shopify Design for wedding invitations

We are a greeting card manufactory, special in wedding invitation
I need a shopify website for our wedding invitation brand. (Lovonna), atttach you can find our logo.
We are looking for someone to create a modern and clean looking e-commerce store for our wedding invitation through Shopify. We need some life, professionalism and style put into our site. We will have a variety serie of products : laser cut wedding invitation, popup wedding invitaiton, vintage wedding invitation, handmade wedding invitation, printing invitation, Custom wedding cards, wedding stationery (including favor box, table card, place card, escort card, number card), Thank you card. our online store requires easy navigation to categories divided by product type.

our market is , Eourpe and USA,
please choose a good color for it.
you can go to our website: www.bluepinecrafts.com and check our product.
also you can go to Shopvane 4 new items.
https://www.shopvane.com/dp/K47T8M2Q61?ref=myi_title_dp

Designs look the same

Target Market(s)

Europe and USA

Industry/Entity Type

wedding

Number of Pages Required

1 page

Requirements
Must have
• Logo, 3 banners than can be changed each 3-5 seconds.
Nice to have
• nice icon and font, beautiful color,

```html
<!DOCTYPE html>
<html lang="en">
<head>
<meta charset="utf-8">
<title>Lovonna – Home and Product Category</title>
<link href="https://fonts.googleapis.com/css2?family=Inter:wght@400;500;600;700&family=Kalam:wght@700&family=Libre+Baskerville:wght@400;700&display=swap" rel="stylesheet">
<style>
:root{
  --canvas:#FBF6E8;
  --white:#FFFFFF;
  --ink:#2A2A2A;
  --muted:#6F6F6F;
  --line:#E6E6E6;
  --navy:#2E3463;
  --brand:#7B3B2D;
  --accent:#E8663D;
  --search:#F1F1F5;
  --cream:#FCF3E0;
  --peach:#FDD5BB;
  --mint:#BFE0CF;
  --sky:#E1F1F4;
  --band:#FAEBD0;
  --form:#FBE1A6;
  --aboutbg:#E4F3F6;
  --lilac:#E2E3EF;
  --photo:#EEEEEF;
  --star:#F2B53C;
}
*{box-sizing:border-box;margin:0;padding:0}
html,body{width:1045px;height:1200px;overflow:hidden;background:var(--canvas)}
body{font-family:"Inter",sans-serif;color:var(--ink)}
.stage{position:absolute;left:0;top:0;width:1792px;height:2060px;transform:scale(0.5825);transform-origin:0 0}
.board-title{position:absolute;top:22px;font-family:"Libre Baskerville",serif;font-size:36px;font-weight:400;transform:translateX(-50%);white-space:nowrap}
.page{position:absolute;top:75px;width:834px;background:var(--white);overflow:hidden}
.page-home{left:46px;height:1985px}
.page-category{left:906px;height:1708px}

/* header */
.logo{position:absolute;left:46px;top:8px;font-family:"Libre Baskerville",serif;font-size:22px;color:var(--brand)}
.search{position:absolute;left:176px;top:10px;width:353px;height:26px;border-radius:13px;background:var(--search);font-size:11px;color:#9A9AA6;padding:6px 0 0 32px}
.search svg{position:absolute;left:10px;top:6px}
.head-icon{position:absolute;top:16px}
.nav{position:absolute;left:0;top:46px;width:100%;height:25px;border-top:1px solid var(--line);border-bottom:2px solid var(--line)}
.nav span{position:absolute;top:5px;font-size:12px}
.nav svg{margin-left:8px;vertical-align:middle}

/* chips */
.chip{position:absolute;width:115px;height:57px;background:var(--white);box-shadow:0 2px 4px rgba(0,0,0,.12);display:flex;align-items:center;gap:8px;padding:0 10px;font-size:9px;line-height:1.15}
.chip i{flex:none;width:20px;height:16px;border-radius:2px;display:block}
.chip.is-active{background:var(--navy);color:var(--white)}
.chip.is-active i{background:#DDE1F2}
.ic-a{background:#F2B8B0}.ic-b{background:#E89A4A}.ic-c{background:#CDE3EE}.ic-d{background:#F1B09B}.ic-e{background:#F3D67A}.ic-f{background:#A9DCC8}

/* home */
.hero{position:absolute;left:23px;top:81px;width:788px;height:290px;background:linear-gradient(120deg,#D9C7AE,#F3E4DA 40%,#EFE0D8 70%,#C9B59A)}
.hero-arrow{position:absolute;top:357px;width:26px;height:26px;border-radius:50%;background:var(--white);box-shadow:0 1px 4px rgba(0,0,0,.25);display:flex;align-items:center;justify-content:center}
.dot{position:absolute;top:367px;width:7px;height:7px;border-radius:50%;background:#D8D8D8}
.dot.is-on{background:var(--accent)}
.section-title{position:absolute;left:0;width:100%;text-align:center;font-family:"Libre Baskerville",serif;font-weight:700;font-size:26px}
.collection{position:absolute;text-align:center}
.collection h3{font-family:"Libre Baskerville",serif;font-weight:400;font-size:23px;margin-top:12px}
.collection a{display:inline-block;font-size:10px;color:var(--ink);text-decoration:underline;margin-top:8px}
.photo{position:absolute}

/* customize band */
.custom{position:absolute;left:0;top:1210px;width:834px;height:232px;background:var(--band)}
.custom-art{position:absolute;left:0;top:60px;width:160px;height:172px;background:linear-gradient(180deg,#F3DDB8,#F0CFA6)}
.custom-paper{position:absolute;left:387px;top:60px;width:80px;height:150px;background:linear-gradient(180deg,#E9DCC4,#EBD2B8)}
.custom h2{position:absolute;left:81px;top:52px;font-family:"Kalam",cursive;font-weight:700;font-size:36px;letter-spacing:.5px;white-space:nowrap}
.custom p.lede{position:absolute;left:81px;top:100px;font-size:15px;line-height:1.15;width:330px}
.form{position:absolute;left:455px;top:14px;width:261px;height:202px;background:var(--form);padding:15px 31px}
.form h4{font-size:11.5px;font-weight:500;color:var(--ink);margin:0 -10px 9px 0;white-space:nowrap}
.field{background:var(--white);height:27px;margin-bottom:6px;font-size:8px;color:#777;padding:9px 10px}
.field.tall{height:56px}
.btn-send{display:inline-block;margin-top:4px;background:var(--navy);color:var(--white);font-size:8px;padding:6px 30px;border-radius:2px}

/* about */
.about-photo{position:absolute;left:0;top:1442px;width:298px;height:232px;background:linear-gradient(135deg,#A98C6A,#E3D8C5 50%,#6D6A63)}
.about{position:absolute;left:298px;top:1442px;width:536px;height:232px;background:var(--aboutbg);padding:45px 63px}
.about h2{font-family:"Libre Baskerville",serif;font-weight:400;font-size:29px;margin-bottom:12px}
.about p{font-size:14.5px;line-height:1.15;width:368px}

/* footer */
.footer-rule{position:absolute;left:31px;width:772px;height:1px;background:var(--line)}
.fcol{position:absolute;font-size:9px;color:#555}
.fcol h5{font-size:12px;font-weight:500;color:var(--ink);margin-bottom:10px}
.fcol li{list-style:none;margin-bottom:8px}
.fcol .contact{display:flex;align-items:center;gap:6px;margin-bottom:14px;color:#777}
.fcol .names{display:flex;flex-wrap:wrap;gap:6px 10px;width:130px;font-size:10px;font-weight:600;color:var(--navy)}
.fcol .names span{display:inline-flex;align-items:center;gap:4px}
.fcol .names b{width:6px;height:6px;background:var(--navy);border-radius:50%;display:inline-block}

/* category page */
.cat-banner{position:absolute;left:47px;top:81px;width:742px;height:185px;background:var(--cream)}
.cat-banner h1{position:absolute;left:19px;top:75px;font-family:"Libre Baskerville",serif;font-weight:700;font-size:31px}
.cat-banner-photo{position:absolute;left:547px;top:8px;width:160px;height:170px;background:linear-gradient(150deg,#C9A47A,#8E2F45 55%,#7A2238);transform:rotate(-8deg);border-radius:4px}
.sort{position:absolute;font-size:10px}
.sort-box{position:absolute;left:707px;top:394px;width:84px;height:24px;border:1px solid var(--line);font-size:8px;color:#666;padding:7px 12px}
.sort-box svg{position:absolute;right:6px;top:8px}
.filter{position:absolute;left:47px;top:449px;width:173px;height:218px;background:var(--lilac)}
.filter-head{background:var(--white);height:32px;font-size:10px;font-weight:500;padding:11px 10px;border:1px solid var(--line)}
.filter h6{font-size:9.5px;font-weight:700;margin:8px 11px 9px}
.filter li{list-style:none;font-size:8.2px;display:flex;align-items:center;gap:7px;margin:0 11px 6px;height:10px}
.box{width:11px;height:11px;border:1px solid #666;background:var(--white);display:block}
.box.is-on{background:#E97A5F;border-color:#E97A5F}
.product{position:absolute;width:133px;height:220px}
.product-photo{position:absolute;left:0;top:0;width:133px;height:127px;background:var(--photo)}
.product-photo::after{content:"";position:absolute;left:28px;top:22px;width:78px;height:82px;border-radius:3px;transform:rotate(-28deg);background:var(--tone)}
.tone-navy{--tone:linear-gradient(135deg,#C79B6A,#2E3767 60%)}
.tone-kraft{--tone:linear-gradient(135deg,#C99B6C,#D9B382 60%)}
.tone-rose{--tone:linear-gradient(135deg,#C79B6A,#8F2D48 60%)}
.tone-gold{--tone:linear-gradient(135deg,#C99B6C,#9C7A3C 60%)}
.product-name{position:absolute;left:8px;top:136px;font-size:10.5px}
.product-price{position:absolute;left:8px;top:157px;font-size:11px;font-weight:700}
.product-rating{position:absolute;right:9px;top:156px;font-size:10px;color:#888}
.product-rating em{color:var(--star);font-style:normal}
.btn-cart{position:absolute;left:8px;top:192px;width:80px;height:19px;background:var(--navy);color:var(--white);font-size:6.5px;display:flex;align-items:center;justify-content:center;gap:3px;border-radius:1px}
.btn-wish{position:absolute;left:99px;top:192px;width:26px;height:19px;border:1px solid var(--accent);display:flex;align-items:center;justify-content:center;border-radius:2px}
.pager{position:absolute;top:1171px;left:660px;font-size:8px;color:#999;display:flex;align-items:center;gap:6px}
.pager .num{border:1px solid var(--line);padding:3px 6px;color:var(--ink)}
.pager .arr{border:1px solid var(--line);width:15px;height:15px;display:flex;align-items:center;justify-content:center;border-radius:3px}
</style>
</head>
<body>
<div class="stage">

  <h2 class="board-title" style="left:463px">Home</h2>
  <h2 class="board-title" style="left:1323px">Product category</h2>

  <!-- ===================== HOME ===================== -->
  <section class="page page-home">
    <header>
      <div class="logo">Lovonna</div>
      <div class="search"><svg width="14" height="14" viewBox="0 0 14 14"><circle cx="6" cy="6" r="4.5" fill="none" stroke="#555" stroke-width="1.4"/><path d="M9.5 9.5L13 13" stroke="#555" stroke-width="1.4"/></svg>Search</div>
      <svg class="head-icon" style="left:711px" width="13" height="13" viewBox="0 0 13 13"><circle cx="6.5" cy="6.5" r="5.7" fill="none" stroke="#333" stroke-width="1.2"/><circle cx="6.5" cy="5" r="2" fill="#333"/><path d="M3 10.5c1-2 6-2 7 0" fill="#333"/></svg>
      <svg class="head-icon" style="left:742px" width="14" height="13" viewBox="0 0 14 13"><path d="M7 12L1.5 6.5A3 3 0 017 2.6 3 3 0 0112.5 6.5z" fill="none" stroke="#333" stroke-width="1.2"/><circle cx="11.5" cy="2" r="2" fill="var(--accent)"/></svg>
      <svg class="head-icon" style="left:772px" width="14" height="13" viewBox="0 0 14 13"><path d="M1 2h2l1.5 6h7l1.5-4.5H4" fill="none" stroke="#333" stroke-width="1.3"/><circle cx="5.5" cy="11" r="1.2" fill="#333"/><circle cx="10.5" cy="11" r="1.2" fill="#333"/><circle cx="12" cy="2" r="2" fill="var(--accent)"/></svg>
      <nav class="nav">
        <span style="left:47px">Home</span>
        <span style="left:102px">Products<svg width="10" height="7" viewBox="0 0 10 7"><path d="M0 0h10L5 7z" fill="#222"/></svg></span>
        <span style="left:192px">News</span>
        <span style="left:246px">About Us</span>
        <span style="left:317px">Contact Us</span>
        <span style="left:398px">Send Inquiry</span>
      </nav>
    </header>

    <div class="hero" role="img" aria-label="Banner photo of wreath-printed wedding invitation cards fanned out on a table"></div>
    <div class="hero-arrow" style="left:358px"><svg width="8" height="10" viewBox="0 0 8 10"><path d="M7 0v10L0 5z" fill="#222"/></svg></div>
    <span class="dot" style="left:392px"></span><span class="dot is-on" style="left:407px"></span><span class="dot" style="left:422px"></span><span class="dot" style="left:437px"></span>
    <div class="hero-arrow" style="left:451px"><svg width="8" height="10" viewBox="0 0 8 10"><path d="M1 0v10l7-5z" fill="#222"/></svg></div>

    <h2 class="section-title" style="top:436px">Explore Categories</h2>
    <div class="chip" style="left:44px;top:481px"><i class="ic-a"></i>Wedding Invitation Card</div>
    <div class="chip" style="left:170px;top:481px"><i class="ic-b"></i>3D Pop Up Card</div>
    <div class="chip" style="left:296px;top:481px"><i class="ic-c"></i>Greeting Card</div>
    <div class="chip" style="left:422px;top:481px"><i class="ic-d"></i>Wedding Stationery</div>
    <div class="chip" style="left:548px;top:481px"><i class="ic-e"></i>Wedding Decoration Accessories</div>
    <div class="chip" style="left:674px;top:481px"><i class="ic-f"></i>Laser Cut Favor Box</div>

    <h2 class="section-title" style="top:629px">Our Collections</h2>

    <div class="collection" style="left:45px;top:673px;width:429px;height:232px;background:var(--cream)">
      <h3>Vintage Card</h3><a href="#">Details</a>
      <div class="photo" role="img" aria-label="Vintage lace invitation set in a box" style="left:17px;top:97px;width:125px;height:125px;background:linear-gradient(135deg,#CFC8BA,#9C9486)"></div>
      <div class="photo" role="img" aria-label="Vintage kraft invitation with lace band" style="left:152px;top:97px;width:125px;height:125px;background:linear-gradient(135deg,#A89A86,#7C6E5E)"></div>
      <div class="photo" role="img" aria-label="Vintage lace pocket invitation with envelope" style="left:287px;top:97px;width:125px;height:125px;background:linear-gradient(135deg,#C8B79E,#8A8272)"></div>
    </div>
    <div class="collection" style="left:485px;top:673px;width:304px;height:232px;background:var(--peach)">
      <h3>Pocket Card</h3><a href="#">Details</a>
      <div class="photo" role="img" aria-label="Burgundy and gold laser-cut pocket invitations with envelopes" style="left:12px;top:82px;width:285px;height:145px;background:linear-gradient(100deg,transparent 5%,#C4906A 15%,#8E2F45 40%,#E9C79E 65%,#D9B58C 85%,transparent 95%);opacity:.85"></div>
    </div>
    <div class="collection" style="left:45px;top:917px;width:304px;height:231px;background:var(--mint)">
      <h3>Laser Cutting Card</h3><a href="#">Details</a>
      <div class="photo" role="img" aria-label="Red laser-cut wedding card on a plate" style="left:13px;top:85px;width:136px;height:136px;background:linear-gradient(135deg,#E8D9CC,#C8262E)"></div>
      <div class="photo" role="img" aria-label="Teal laser-cut wedding card with flowers" style="left:154px;top:85px;width:135px;height:136px;background:linear-gradient(135deg,#EDE3E2,#3BA08A)"></div>
    </div>
    <div class="collection" style="left:360px;top:917px;width:429px;height:231px;background:var(--sky)">
      <h3>Pop Up Card</h3><a href="#">Details</a>
      <div class="photo" role="img" aria-label="Navy pop up wedding card" style="left:15px;top:96px;width:126px;height:126px;background:linear-gradient(135deg,#2B355E,#D9D6CE)"></div>
      <div class="photo" role="img" aria-label="Green and red pop up holiday card" style="left:152px;top:96px;width:126px;height:126px;background:linear-gradient(135deg,#F1F1EF,#2E9A7E 60%,#C8393C)"></div>
      <div class="photo" role="img" aria-label="Red pop up Christmas card" style="left:289px;top:96px;width:126px;height:126px;background:linear-gradient(135deg,#F4F1F1,#B82026)"></div>
    </div>

    <div class="custom">
      <div class="custom-art" role="img" aria-label="Illustration of craft tools and paper"></div>
      <div class="custom-paper" role="img" aria-label="Illustration of coloured paper sheets"></div>
      <h2>Customize Your Card</h2>
      <p class="lede">Have your own design ? or want something to be more special ?</p>
      <div class="form">
        <h4>Let’s talk more about what you need</h4>
        <div class="field">Your Name</div>
        <div class="field">Your Phone Number/E-mail</div>
        <div class="field tall">Message</div>
        <span class="btn-send">Send</span>
      </div>
    </div>

    <div class="about-photo" role="img" aria-label="Photo of a team working together in a library"></div>
    <div class="about">
      <h2>About Us</h2>
      <p>Lorem ipsum dolor sit amet, consectetur adipiscing elit. Interdum convallis risus eget scelerisque. Massa quis tellus adipiscing ac vel, id vitae, leo. Quis mattis vestib morbi commodo. Eget consequat, pellentes adipiscing eu fringilla at. Eget eget tempus consectetur urna orci amet. Tellus ultrices et tempus lectus etiam.</p>
    </div>

    <div class="footer-rule" style="top:1709px"></div>
    <div class="fcol" style="left:54px;top:1775px">
      <h5>About</h5>
      <p class="contact"><svg width="10" height="12" viewBox="0 0 10 12"><path d="M5 11.5S1 7 1 4.5a4 4 0 018 0C9 7 5 11.5 5 11.5z" fill="none" stroke="#666"/><circle cx="5" cy="4.5" r="1.4" fill="none" stroke="#666"/></svg>Harbor Vale, 510882</p>
      <p class="contact"><svg width="11" height="11" viewBox="0 0 11 11"><path d="M2 1l2 .3.8 2.4-1.3 1a6 6 0 002.8 2.8l1-1.3 2.4.8.3 2c-4 .8-9-4.2-8-8z" fill="none" stroke="#666"/></svg>02 5550 1937</p>
      <p class="contact"><svg width="12" height="9" viewBox="0 0 12 9"><rect x=".5" y=".5" width="11" height="8" fill="none" stroke="#666"/><path d="M.5 .5L6 5l5.5-4.5" fill="none" stroke="#666"/></svg>Admin@bluepinecrafts.com</p>
    </div>
    <div class="fcol" style="left:292px;top:1775px"><h5>Quick Access</h5><ul><li>Home</li><li>Products</li><li>News</li><li>About Us</li><li>Contact Us</li><li>Send Inquiry</li></ul></div>
    <div class="fcol" style="left:395px;top:1775px"><h5>Category</h5><ul><li>Wedding Invitation Card</li><li>3D Pop Up Card</li><li>Greeting Card</li><li>Wedding Stationary</li><li>Wedding Decoration</li><li>Laser Cut Favor Box</li></ul></div>
    <div class="fcol" style="left:529px;top:1775px"><h5>Share</h5><div class="names" style="width:95px"><span>Friendly</span><span>Chirp</span><span>Snapbox</span><span>Workline</span></div></div>
    <div class="fcol" style="left:642px;top:1775px"><h5>Payment Methods</h5><div class="names"><span><b></b>Cardora</span><span>Amexa</span><span>Unipay</span><span>Vistra</span><span>Paypond</span></div></div>
  </section>

  <!-- ===================== PRODUCT CATEGORY ===================== -->
  <section class="page page-category">
    <header>
      <div class="logo">Lovonna</div>
      <div class="search"><svg width="14" height="14" viewBox="0 0 14 14"><circle cx="6" cy="6" r="4.5" fill="none" stroke="#555" stroke-width="1.4"/><path d="M9.5 9.5L13 13" stroke="#555" stroke-width="1.4"/></svg>Search</div>
      <svg class="head-icon" style="left:711px" width="13" height="13" viewBox="0 0 13 13"><circle cx="6.5" cy="6.5" r="5.7" fill="none" stroke="#333" stroke-width="1.2"/><circle cx="6.5" cy="5" r="2" fill="#333"/><path d="M3 10.5c1-2 6-2 7 0" fill="#333"/></svg>
      <svg class="head-icon" style="left:742px" width="14" height="13" viewBox="0 0 14 13"><path d="M7 12L1.5 6.5A3 3 0 017 2.6 3 3 0 0112.5 6.5z" fill="none" stroke="#333" stroke-width="1.2"/><circle cx="11.5" cy="2" r="2" fill="var(--accent)"/></svg>
      <svg class="head-icon" style="left:772px" width="14" height="13" viewBox="0 0 14 13"><path d="M1 2h2l1.5 6h7l1.5-4.5H4" fill="none" stroke="#333" stroke-width="1.3"/><circle cx="5.5" cy="11" r="1.2" fill="#333"/><circle cx="10.5" cy="11" r="1.2" fill="#333"/><circle cx="12" cy="2" r="2" fill="var(--accent)"/></svg>
      <nav class="nav">
        <span style="left:47px">Home</span>
        <span style="left:102px">Products<svg width="10" height="7" viewBox="0 0 10 7"><path d="M0 0h10L5 7z" fill="#222"/></svg></span>
        <span style="left:192px">News</span>
        <span style="left:246px">About Us</span>
        <span style="left:317px">Contact Us</span>
        <span style="left:398px">Send Inquiry</span>
      </nav>
    </header>

    <div class="cat-banner">
      <h1>Wedding Invitation Card</h1>
      <div class="cat-banner-photo" role="img" aria-label="Burgundy laser-cut pocket invitation on a kraft envelope"></div>
    </div>

    <div class="chip is-active" style="left:45px;top:302px"><i></i>Wedding Invitation Card</div>
    <div class="chip" style="left:171px;top:302px"><i class="ic-b"></i>3D Pop Up Card</div>
    <div class="chip" style="left:297px;top:302px"><i class="ic-c"></i>Greeting Card</div>
    <div class="chip" style="left:423px;top:302px"><i class="ic-d"></i>Wedding Stationery</div>
    <div class="chip" style="left:549px;top:302px"><i class="ic-e"></i>Wedding Decoration Accessories</div>
    <div class="chip" style="left:675px;top:302px"><i class="ic-f"></i>Laser Cut Favor Box</div>

    <span class="sort" style="left:669px;top:400px">Set by</span>
    <div class="sort-box">Popularity<svg width="10" height="7" viewBox="0 0 10 7"><path d="M0 0h10L5 7z" fill="#222"/></svg></div>

    <aside class="filter">
      <div class="filter-head">CATEGORY</div>
      <h6>WEDDING INVITATION CARD</h6>
      <ul>
        <li><span class="box is-on"></span>All</li>
        <li><span class="box"></span>Laser cut wedding invitation</li>
        <li><span class="box"></span>Popup wedding invitation</li>
        <li><span class="box"></span>Vintage wedding invitation</li>
        <li><span class="box"></span>Handmade wedding invitation</li>
        <li><span class="box"></span>Pocket wedding invitation</li>
        <li><span class="box"></span>Handmade wedding invitation</li>
        <li><span class="box"></span>Acrylic wedding invitation</li>
        <li><span class="box"></span>Custom wedding invitation</li>
      </ul>
    </aside>

    <div class="product" style="left:235px;top:449px"><div class="product-photo tone-navy" role="img" aria-label="Navy laser-cut invitation on kraft envelope"></div><p class="product-name">Product Name</p><p class="product-price">$2.4</p><p class="product-rating"><em>★</em> (4.9)</p><span class="btn-cart">🛒 Add to Cart</span><span class="btn-wish"><svg width="11" height="10" viewBox="0 0 14 13"><path d="M7 12L1.5 6.5A3 3 0 017 2.6 3 3 0 0112.5 6.5z" fill="none" stroke="#E8663D" stroke-width="1.4"/></svg></span></div>
    <div class="product" style="left:376px;top:449px;box-shadow:0 2px 6px rgba(0,0,0,.15)"><div class="product-photo tone-kraft" role="img" aria-label="Gold laser-cut invitation on kraft envelope"></div><p class="product-name">Sweet Calendula</p><p class="product-price">$2.4</p><p class="product-rating"><em>★</em> (4.9)</p><span class="btn-cart">🛒 Add to Cart</span><span class="btn-wish"><svg width="11" height="10" viewBox="0 0 14 13"><path d="M7 12L1.5 6.5A3 3 0 017 2.6 3 3 0 0112.5 6.5z" fill="#E8663D"/></svg></span></div>
    <div class="product" style="left:517px;top:449px"><div class="product-photo tone-rose" role="img" aria-label="Burgundy pocket invitation on kraft envelope"></div><p class="product-name">Elegant Rosse</p><p class="product-price">$2.4</p><p class="product-rating"><em>★</em> (4.9)</p><span class="btn-cart">🛒 Add to Cart</span><span class="btn-wish"><svg width="11" height="10" viewBox="0 0 14 13"><path d="M7 12L1.5 6.5A3 3 0 017 2.6 3 3 0 0112.5 6.5z" fill="none" stroke="#E8663D" stroke-width="1.4"/></svg></span></div>
    <div class="product" style="left:659px;top:449px"><div class="product-photo tone-gold" role="img" aria-label="Gold lace invitation on kraft envelope"></div><p class="product-name">Aladdin Bride</p><p class="product-price">$2.4</p><p class="product-rating"><em>★</em> (4.9)</p><span class="btn-cart">🛒 Add to Cart</span><span class="btn-wish"><svg width="11" height="10" viewBox="0 0 14 13"><path d="M7 12L1.5 6.5A3 3 0 017 2.6 3 3 0 0112.5 6.5z" fill="none" stroke="#E8663D" stroke-width="1.4"/></svg></span></div>

    <div class="product" style="left:235px;top:687px"><div class="product-photo tone-navy" role="img" aria-label="Navy laser-cut invitation on kraft envelope"></div><p class="product-name">Product Name</p><p class="product-price">$2.4</p><p class="product-rating"><em>★</em> (4.9)</p><span class="btn-cart">🛒 Add to Cart</span><span class="btn-wish"><svg width="11" height="10" viewBox="0 0 14 13"><path d="M7 12L1.5 6.5A3 3 0 017 2.6 3 3 0 0112.5 6.5z" fill="none" stroke="#E8663D" stroke-width="1.4"/></svg></span></div>
    <div class="product" style="left:376px;top:687px"><div class="product-photo tone-kraft" role="img" aria-label="Gold laser-cut invitation on kraft envelope"></div><p class="product-name">Sweet Calendula</p><p class="product-price">$2.4</p><p class="product-rating"><em>★</em> (4.9)</p><span class="btn-cart">🛒 Add to Cart</span><span class="btn-wish"><svg width="11" height="10" viewBox="0 0 14 13"><path d="M7 12L1.5 6.5A3 3 0 017 2.6 3 3 0 0112.5 6.5z" fill="#E8663D"/></svg></span></div>
    <div class="product" style="left:517px;top:687px"><div class="product-photo tone-rose" role="img" aria-label="Burgundy pocket invitation on kraft envelope"></div><p class="product-name">Elegant Rosse</p><p class="product-price">$2.4</p><p class="product-rating"><em>★</em> (4.9)</p><span class="btn-cart">🛒 Add to Cart</span><span class="btn-wish"><svg width="11" height="10" viewBox="0 0 14 13"><path d="M7 12L1.5 6.5A3 3 0 017 2.6 3 3 0 0112.5 6.5z" fill="none" stroke="#E8663D" stroke-width="1.4"/></svg></span></div>
    <div class="product" style="left:659px;top:687px"><div class="product-photo tone-gold" role="img" aria-label="Gold lace invitation on kraft envelope"></div><p class="product-name">Aladdin Bride</p><p class="product-price">$2.4</p><p class="product-rating"><em>★</em> (4.9)</p><span class="btn-cart">🛒 Add to Cart</span><span class="btn-wish"><svg width="11" height="10" viewBox="0 0 14 13"><path d="M7 12L1.5 6.5A3 3 0 017 2.6 3 3 0 0112.5 6.5z" fill="none" stroke="#E8663D" stroke-width="1.4"/></svg></span></div>

    <div class="product" style="left:235px;top:925px"><div class="product-photo tone-navy" role="img" aria-label="Navy laser-cut invitation on kraft envelope"></div><p class="product-name">Product Name</p><p class="product-price">$2.4</p><p class="product-rating"><em>★</em> (4.9)</p><span class="btn-cart">🛒 Add to Cart</span><span class="btn-wish"><svg width="11" height="10" viewBox="0 0 14 13"><path d="M7 12L1.5 6.5A3 3 0 017 2.6 3 3 0 0112.5 6.5z" fill="none" stroke="#E8663D" stroke-width="1.4"/></svg></span></div>
    <div class="product" style="left:376px;top:925px"><div class="product-photo tone-kraft" role="img" aria-label="Gold laser-cut invitation on kraft envelope"></div><p class="product-name">Sweet Calendula</p><p class="product-price">$2.4</p><p class="product-rating"><em>★</em> (4.9)</p><span class="btn-cart">🛒 Add to Cart</span><span class="btn-wish"><svg width="11" height="10" viewBox="0 0 14 13"><path d="M7 12L1.5 6.5A3 3 0 017 2.6 3 3 0 0112.5 6.5z" fill="#E8663D"/></svg></span></div>
    <div class="product" style="left:517px;top:925px"><div class="product-photo tone-rose" role="img" aria-label="Burgundy pocket invitation on kraft envelope"></div><p class="product-name">Elegant Rosse</p><p class="product-price">$2.4</p><p class="product-rating"><em>★</em> (4.9)</p><span class="btn-cart">🛒 Add to Cart</span><span class="btn-wish"><svg width="11" height="10" viewBox="0 0 14 13"><path d="M7 12L1.5 6.5A3 3 0 017 2.6 3 3 0 0112.5 6.5z" fill="none" stroke="#E8663D" stroke-width="1.4"/></svg></span></div>
    <div class="product" style="left:659px;top:925px"><div class="product-photo tone-gold" role="img" aria-label="Gold lace invitation on kraft envelope"></div><p class="product-name">Aladdin Bride</p><p class="product-price">$2.4</p><p class="product-rating"><em>★</em> (4.9)</p><span class="btn-cart">🛒 Add to Cart</span><span class="btn-wish"><svg width="11" height="10" viewBox="0 0 14 13"><path d="M7 12L1.5 6.5A3 3 0 017 2.6 3 3 0 0112.5 6.5z" fill="none" stroke="#E8663D" stroke-width="1.4"/></svg></span></div>

    <div class="pager">Page <span class="num">10</span> of 50
      <span class="arr"><svg width="5" height="8" viewBox="0 0 5 8"><path d="M4 0L0 4l4 4" fill="none" stroke="#333"/></svg></span>
      <span class="arr"><svg width="5" height="8" viewBox="0 0 5 8"><path d="M1 0l4 4-4 4" fill="none" stroke="#333"/></svg></span>
    </div>

    <div class="custom">
      <div class="custom-art" role="img" aria-label="Illustration of craft tools and paper"></div>
      <div class="custom-paper" role="img" aria-label="Illustration of coloured paper sheets"></div>
      <h2>Customize Your Card</h2>
      <p class="lede">Have your own design ? or want something to be more special ?</p>
      <div class="form">
        <h4>Let’s talk more about what you need</h4>
        <div class="field">Your Name</div>
        <div class="field">Your Phone Number/E-mail</div>
        <div class="field tall">Message</div>
        <span class="btn-send">Send</span>
      </div>
    </div>

    <div class="footer-rule" style="top:1477px"></div>
    <div class="fcol" style="left:55px;top:1543px">
      <h5>About</h5>
      <p class="contact"><svg width="10" height="12" viewBox="0 0 10 12"><path d="M5 11.5S1 7 1 4.5a4 4 0 018 0C9 7 5 11.5 5 11.5z" fill="none" stroke="#666"/><circle cx="5" cy="4.5" r="1.4" fill="none" stroke="#666"/></svg>Harbor Vale, 510882</p>
      <p class="contact"><svg width="11" height="11" viewBox="0 0 11 11"><path d="M2 1l2 .3.8 2.4-1.3 1a6 6 0 002.8 2.8l1-1.3 2.4.8.3 2c-4 .8-9-4.2-8-8z" fill="none" stroke="#666"/></svg>02 5550 1937</p>
      <p class="contact"><svg width="12" height="9" viewBox="0 0 12 9"><rect x=".5" y=".5" width="11" height="8" fill="none" stroke="#666"/><path d="M.5 .5L6 5l5.5-4.5" fill="none" stroke="#666"/></svg>Admin@bluepinecrafts.com</p>
    </div>
    <div class="fcol" style="left:293px;top:1543px"><h5>Quick Access</h5><ul><li>Home</li><li>Products</li><li>News</li><li>About Us</li><li>Contact Us</li><li>Send Inquiry</li></ul></div>
    <div class="fcol" style="left:396px;top:1543px"><h5>Category</h5><ul><li>Wedding Invitation Card</li><li>3D Pop Up Card</li><li>Greeting Card</li><li>Wedding Stationary</li><li>Wedding Decoration</li><li>Laser Cut Favor Box</li></ul></div>
    <div class="fcol" style="left:529px;top:1543px"><h5>Share</h5><div class="names" style="width:95px"><span>Friendly</span><span>Chirp</span><span>Snapbox</span><span>Workline</span></div></div>
    <div class="fcol" style="left:643px;top:1543px"><h5>Payment Methods</h5><div class="names"><span><b></b>Cardora</span><span>Amexa</span><span>Unipay</span><span>Vistra</span><span>Paypond</span></div></div>
  </section>

</div>
</body>
</html>
```